Im want a website LIKE KVT's and FieldCrest.com's with product payment options like Trovella's

I need a website LIKE KVT with a header made EXACTLY LIKE THAT OF FIELDCRESTS .

The front page photo should be like that of FIELDCREST's webpage as well.

The name of the website will be called "M.K. (Maravel Key)".

We will be targeting ALL MARKETS in a small town in central Panama and charging businesses "listing fees" like a phone book does but also providing informational blogs, news, and other interesting activities.

THIS IS A MULTI PAGE WEBSITE

THIS IS WHERE KVT's website meets Zentaro/FieldCrest.

Once the layout is built I will tweak and modify, add information, and upload items for sale.

Here is a list of specific categories that should be listed out above the front page header image/search bar

-- Home -- News -- Travel -- Activities -- Shop & Dine -- Store -- More... --

These categories should be spread across the bottom of the page in three sections:

WHATS SO GREAT ABOUT (Maravel Key),
HAND PICKED TOURS
ACTIVITIES etc.

Also lets use www.Trovella.example 's
"HOT DESTINATIONS"
"BEAT THE BEST PRICES IN BOQUETE"
"OCTOBERS INSIDER PICKS"
"TOP DESTINATIONS"
and spread them in four sections side-by-side near the bottom of the page.

Overall I would like to see the finished product to be something LIKE KVT's and FieldCrests.

WE NEED ONLINE PAYMENT OPTIONS LIKE ZENTARO'S WEBSITE HAS

This will be a desktop website but should be very mobile friendly as well.

-roderick

P.S. Good luck!

If it isn't already too late to change the website name, the name of the website should be "Maravel Key". Added Friday, October 9, 2015

What do you guys think the budget should be to win this? Added Saturday, October 10, 2015

www.lunavista.example is the most amazing simple site. Whoever can make me a replica with my specifications will win immediately!!!! Added Sunday, October 18, 2015

OMG www.lunavista.example is the bomb!So simple and elegant. Whoever can make me an EXACT REPLICA OF WWW.LUNAVISTA.EXAMPLE as my site with the specifications mentioned in my brief will take home the $825.00 immediately! Good luck amigos! Added Sunday, October 18, 2015

Does anybody know how to add recurring monthly billing options on this website? Added Sunday, October 18, 2015

ALL MARKETS

Product

Coded - Design and coding required

5+ page

• Paywell payment options.
• I must be able to add and remove photos/text and video from the HTML files in the page.
• Be creative my friends, and may the odds be forever in your favor!
• I added some photos of a good layout for our page below.

```html
<!DOCTYPE html>
<html lang="en">
<head>
<meta charset="utf-8">
<title>Maravel Key</title>
<link rel="stylesheet" href="https://fonts.googleapis.com/css2?family=Montserrat:wght@400;600;700;800&family=Open+Sans:wght@400;600&display=swap">
<style>
:root{
  --red:#e3120b;
  --red-dark:#c40e08;
  --ink:#222;
  --grey:#777;
  --line:#cfcfcf;
  --white:#fff;
  --bg:#ffffff;
}
*{box-sizing:border-box;margin:0;padding:0}
html,body{width:1200px;height:2896px;overflow:hidden;background:var(--bg)}
body{font-family:"Open Sans",Arial,sans-serif;color:var(--ink);position:relative}
.site-header{position:absolute;top:0;left:0;width:1200px;height:72px;background:var(--white);display:flex;align-items:center;box-shadow:0 1px 3px rgba(0,0,0,.15);z-index:2}
.brand{position:absolute;left:32px;top:4px;width:60px;height:60px;background:var(--red);color:var(--white);font-family:"Montserrat",sans-serif;font-weight:800;font-size:22px;display:flex;align-items:center;justify-content:center}
.main-nav{position:absolute;left:450px;top:22px;display:flex}
.main-nav a{font-family:"Montserrat",sans-serif;font-size:12px;font-weight:600;color:#555;text-decoration:none;padding:6px 20px;border-right:1px solid #ddd;letter-spacing:.5px}
.main-nav a.active{background:#eee;color:var(--ink)}
.search{position:absolute;left:1040px;top:22px;width:118px;height:26px;border:1px solid #ccc;display:flex;align-items:center;justify-content:flex-end;padding-right:6px}
.hero{position:absolute;top:72px;left:0;width:1200px;height:448px;background:linear-gradient(180deg,#c9a7c9 0%,#e8a7b0 35%,#d78a7e 55%,#8a4a3f 80%,#4a3a44 100%)}
.hero-copy{position:absolute;left:100px;top:176px;width:480px}
.hero-title{font-family:"Montserrat",sans-serif;font-weight:800;font-size:40px;line-height:42px;color:var(--white);text-transform:uppercase}
.hero-sub{margin-top:12px;font-size:13px;line-height:18px;color:#ffd0cc;width:360px}
.btn{display:inline-block;background:var(--red);color:var(--white);font-family:"Montserrat",sans-serif;font-size:13px;font-weight:600;padding:8px 22px;border:none}
.hero .btn{margin-top:18px}
.login{position:absolute;left:840px;top:188px;width:280px;height:228px;background:rgba(255,255,255,.88);padding:20px 24px}
.login h3{font-family:"Montserrat",sans-serif;font-size:22px;font-weight:700;margin-bottom:14px}
.field{height:26px;border:1px solid #ccc;background:var(--white);font-size:11px;color:#999;padding:5px 8px;margin-bottom:8px}
.forgot{font-size:10px;color:#888;text-align:right;margin-bottom:12px}
.section-title{position:absolute;left:72px;width:1056px;display:flex;align-items:center;gap:24px;font-family:"Montserrat",sans-serif;font-size:30px;color:#666}
.section-title::before,.section-title::after{content:"";flex:1;height:1px;background:var(--line)}
.more-link{position:absolute;left:72px;width:1056px;display:flex;align-items:center;gap:20px;font-size:14px;color:#666}
.more-link::before,.more-link::after{content:"";flex:1;height:1px;background:var(--line)}
.categories{position:absolute;left:72px;top:680px;font-size:13px;line-height:20px}
.categories h4{font-size:14px;font-weight:600;margin-bottom:4px}
.categories li{list-style:none;color:#555}
.categories li.current{color:var(--red)}
.news-list{position:absolute;left:288px;top:688px;display:flex;gap:16px}
.news-card{width:266px}
.news-photo{height:200px}
.news-card h5{font-size:14px;font-weight:600;margin-top:10px}
.news-card p{font-size:11px;line-height:15px;color:var(--grey);margin-top:4px}
.banner{position:absolute;top:1144px;left:0;width:1200px;height:356px;background:linear-gradient(180deg,#3f7fd0 0%,#8cc0ec 40%,#2f7a3a 62%,#37c0c8 72%,#1aa3c0 100%)}
.travel-list{position:absolute;top:1640px;left:52px;width:1096px;display:flex;justify-content:space-between}
.travel-item{width:250px;text-align:center}
.travel-photo{width:240px;height:240px;border-radius:50%;margin:0 auto}
.travel-item p{margin-top:16px;font-size:16px;color:#444}
.activity-grid{position:absolute;top:2140px;left:72px;width:1056px;display:grid;grid-template-columns:repeat(4,1fr);gap:16px 8px}
.activity-tile{height:128px;position:relative}
.activity-tile span{position:absolute;left:0;bottom:0;width:100%;height:34px;background:rgba(227,18,11,.92);color:var(--white);font-family:"Montserrat",sans-serif;font-size:13px;font-weight:600;padding:9px 12px}
.site-footer{position:absolute;top:2544px;left:0;width:1200px;height:306px;background:var(--red);color:var(--white)}
.footer-nav{position:absolute;left:144px;top:64px;list-style:none;font-size:12px;line-height:22px}
.footer-contact{position:absolute;left:336px;top:64px;font-size:12px;line-height:22px}
.footer-news{position:absolute;left:572px;top:56px;width:260px}
.socials{display:flex;gap:10px;margin-bottom:14px}
.socials i{width:22px;height:22px;border-radius:50%;background:var(--white);display:block}
.footer-news label{font-size:11px;font-weight:600;display:block;margin-bottom:6px}
.footer-news .field{width:210px;color:#aaa}
.footer-news .btn{background:var(--white);color:var(--red);margin-top:6px}
.footer-brand{position:absolute;left:852px;top:130px;font-family:"Montserrat",sans-serif;font-weight:700;font-size:34px;color:var(--white)}
.legal{position:absolute;top:2850px;left:0;width:1200px;height:46px;text-align:center;font-size:11px;color:#999;padding-top:16px}
</style>
</head>
<body>
<header class="site-header">
  <div class="brand">MK</div>
  <nav class="main-nav">
    <a class="active">HOME</a><a>NEWS</a><a>TRAVEL</a><a>ACTIVITIES</a><a>SHOP &amp; DINE</a><a>STORE</a>
  </nav>
  <div class="search"><svg width="14" height="14" viewBox="0 0 14 14"><circle cx="6" cy="6" r="4.5" fill="none" stroke="#333" stroke-width="1.6"/><line x1="9.3" y1="9.3" x2="13" y2="13" stroke="#333" stroke-width="1.8"/></svg></div>
</header>

<section class="hero" role="img" aria-label="Sunset over a rocky coastline and turquoise bay">
  <div class="hero-copy">
    <h1 class="hero-title">Sed ut perspiciatis unde omnis iste natus error sit</h1>
    <p class="hero-sub">Lorem ipsum dolor sit amet consectetur adipiscing elit sed do eiusmod tempor incididunt ut labore</p>
    <span class="btn">Read more</span>
  </div>
  <form class="login">
    <h3>Login</h3>
    <div class="field">Username</div>
    <div class="field">Password</div>
    <div class="forgot">Forgot your password?</div>
    <span class="btn">Login</span>
  </form>
</section>

<h2 class="section-title" style="top:534px">News</h2>
<aside class="categories">
  <h4>Categories</h4>
  <ul>
    <li class="current">Category 1</li><li>Category 2</li><li>Category 3</li><li>Category 4</li><li>Category 5</li><li>Category 6</li><li>Category 7</li>
  </ul>
</aside>
<div class="news-list">
  <article class="news-card">
    <div class="news-photo" role="img" aria-label="Hammock between palm trees on a beach" style="background:linear-gradient(180deg,#6fb6e6,#9fd3ea 55%,#d9c9a0)"></div>
    <h5>Lorem ipsum dolor sit amet</h5>
    <p>Sed ut perspiciatis unde omnis iste natus error sit voluptatem accusantium doloremque laudantium totam rem aperiam.</p>
  </article>
  <article class="news-card">
    <div class="news-photo" role="img" aria-label="Resort pool surrounded by palms" style="background:linear-gradient(180deg,#8fc3e8,#4f8f5a 45%,#45b7d6)"></div>
    <h5>Lorem ipsum dolor sit amet</h5>
    <p>Sed ut perspiciatis unde omnis iste natus error sit voluptatem accusantium doloremque laudantium totam rem aperiam.</p>
  </article>
  <article class="news-card">
    <div class="news-photo" role="img" aria-label="Friends walking together on the beach" style="background:linear-gradient(180deg,#9cc2d8,#c9a48a 55%,#d8c6a6)"></div>
    <h5>Lorem ipsum dolor sit amet</h5>
    <p>Sed ut perspiciatis unde omnis iste natus error sit voluptatem accusantium doloremque laudantium totam rem aperiam.</p>
  </article>
</div>
<div class="more-link" style="top:1074px">Read all</div>

<div class="banner" role="img" aria-label="Palm-covered island in clear turquoise water"></div>

<h2 class="section-title" style="top:1522px">Travel</h2>
<div class="travel-list">
  <div class="travel-item"><div class="travel-photo" role="img" aria-label="Beach with thatched umbrellas" style="background:radial-gradient(circle at 50% 40%,#7fc3e6,#3b8fb8 60%,#d9c08a)"></div><p>Exotic Destinations</p></div>
  <div class="travel-item"><div class="travel-photo" role="img" aria-label="Green islands in a lagoon" style="background:radial-gradient(circle at 50% 40%,#a9d6ef,#4e9a5c 55%,#2fa7c4)"></div><p>Explore the outskirts</p></div>
  <div class="travel-item"><div class="travel-photo" role="img" aria-label="Jumping on the sand at sunset" style="background:radial-gradient(circle at 50% 40%,#f2dca8,#d7b27a 60%,#b58a5a)"></div><p>Let go of yourself</p></div>
  <div class="travel-item"><div class="travel-photo" role="img" aria-label="Relaxing in a beach chair" style="background:radial-gradient(circle at 50% 40%,#8cc8ef,#e07a5a 55%,#3f96d0)"></div><p>Cherish the moments</p></div>
</div>

<h2 class="section-title" style="top:2046px">Activites</h2>
<div class="activity-grid">
  <div class="activity-tile" role="img" aria-label="Beach party" style="background:linear-gradient(135deg,#f3c27a,#c55a3a)"><span>Link 1</span></div>
  <div class="activity-tile" role="img" aria-label="Group on the sand" style="background:linear-gradient(135deg,#d9b38a,#8a5a44)"><span>Link 2</span></div>
  <div class="activity-tile" role="img" aria-label="Boat trip" style="background:linear-gradient(135deg,#8fd3e8,#2d8fb5)"><span>Link 3</span></div>
  <div class="activity-tile" role="img" aria-label="Snorkelling" style="background:linear-gradient(135deg,#4fc1de,#1a6f9c)"><span>Link 4</span></div>
  <div class="activity-tile" role="img" aria-label="Jet ski ride" style="background:linear-gradient(135deg,#7ab8d8,#b5403a)"><span>Link 5</span></div>
  <div class="activity-tile" role="img" aria-label="Kayaking" style="background:linear-gradient(135deg,#5fb0d6,#2a6a9a)"><span>Link 6</span></div>
  <div class="activity-tile" role="img" aria-label="Speed boat" style="background:linear-gradient(135deg,#a9d8ea,#1e7fb0)"><span>Link 7</span></div>
  <div class="activity-tile" role="img" aria-label="Kitesurfing" style="background:linear-gradient(135deg,#9fd6ee,#3aa0d0)"><span>Link 8</span></div>
</div>
<div class="more-link" style="top:2486px">View all</div>

<footer class="site-footer">
  <ul class="footer-nav"><li>HOME</li><li>NEWS</li><li>TRAVEL</li><li>ACTIVITIES</li><li>SHOP &amp; DINE</li><li>STORE</li></ul>
  <div class="footer-contact"><p>SAMPLE ADDRESS</p><p>+507 555 0142</p><p>INFO@MARAVELKEY.EXAMPLE</p></div>
  <div class="footer-news">
    <div class="socials"><i></i><i></i><i></i><i></i><i></i></div>
    <label>SUBSCRIBE TO OUR NEWSLETTER</label>
    <div class="field">Email address</div>
    <span class="btn">Subscribe</span>
  </div>
  <div class="footer-brand">Maravel Key</div>
</footer>
<p class="legal">© 2015 Maravel Key. All rights reserved.</p>
</body>
</html>
```